Sunny Paths and joy Business card

I have a logo, but will like a business card design. Is for a travel agency in Mexico. We focus in family experiences.

I will liek some thing different and unique, from the traditional business card, something to get remmeber for.

Business card information:

Leandro T. Ocampo
leandro@sunnypathsjoy.example

Alameda 482, 3 piso
Col. Tlalpizco
Mexico, D.F. 07320

office: (55) 5000-0142
mobile: (55) 9000-0187

www.sunnypathsjoy.example
@sunnypjoy
blog: sunnypathsandjoy.blogsite.example
facebook: SunnyPathsAndJoy

```html
<!DOCTYPE html>
<html lang="en">
<head>
<meta charset="utf-8">
<title>Sunny Paths and joy – Business card</title>
<link rel="stylesheet" href="https://fonts.googleapis.com/css2?family=Arimo:wght@400;700&display=swap">
<style>
  :root {
    --page: #dfe4e8;
    --blue-deep: #0f6db5;
    --blue: #1d86d0;
    --blue-light: #3aa6e6;
    --blue-pale: #d9ecf8;
    --yellow: #f6b81c;
    --orange: #f08a1c;
    --sea: #6cc6d8;
    --sand: #ece6d6;
    --ink: #3b3f44;
    --link: #1f7fd0;
    --white: #ffffff;
  }
  * { margin: 0; padding: 0; box-sizing: border-box; }
  html, body { width: 1200px; height: 960px; overflow: hidden; }
  body {
    background: var(--page);
    font-family: "Arimo", Arial, sans-serif;
    position: relative;
  }
  .card {
    position: absolute;
    left: 220px;
    width: 760px;
    height: 434px;
    overflow: hidden;
    box-shadow: 0 6px 18px rgba(0,0,0,.18);
  }
  .card-front { top: 36px; }
  .card-back { top: 492px; background: var(--white); }
  .card svg.art { position: absolute; inset: 0; }

  .front-url {
    position: absolute; left: 40px; top: 34px;
    color: var(--white); font-weight: 700; font-size: 27px;
  }
  .front-logo {
    position: absolute; left: 92px; top: 186px; width: 270px; height: 180px;
    display: flex; align-items: center; justify-content: center; text-align: center;
    color: var(--blue-deep); font-weight: 700; font-size: 34px; line-height: 1.05;
  }

  .back-name {
    position: absolute; left: 64px; top: 64px;
    font-size: 26px; color: var(--ink); letter-spacing: .5px;
  }
  .contact-list {
    position: absolute; left: 40px; top: 214px; list-style: none;
    font-size: 18px; color: var(--ink); line-height: 24px;
  }
  .contact-list li { display: flex; align-items: center; }
  .contact-list svg { width: 14px; height: 14px; margin-right: 20px; flex: none; }
  .contact-list .web { color: var(--link); }
  .address {
    position: absolute; left: 500px; top: 262px; list-style: none;
    font-size: 17px; color: var(--ink); line-height: 22px;
  }
  .address .social { display: flex; align-items: center; }
  .address .social i {
    display: inline-block; width: 11px; height: 11px; background: var(--link);
    margin-right: 14px;
  }
  .back-logo {
    position: absolute; left: 538px; top: 60px; width: 186px; height: 92px;
    display: flex; align-items: center; justify-content: center; text-align: center;
    color: var(--blue-deep); font-weight: 700; font-size: 22px; line-height: 1.05;
  }
</style>
</head>
<body>

<section class="card card-front">
  <svg class="art" width="760" height="434" viewBox="0 0 760 434">
    <defs>
      <radialGradient id="frontGlow" cx="0.45" cy="0.45" r="0.8">
        <stop offset="0" stop-color="#2a95dc"/>
        <stop offset="1" stop-color="#0f6db5"/>
      </radialGradient>
      <linearGradient id="beachTone" x1="0" y1="0" x2="0" y2="1">
        <stop offset="0" stop-color="#8fd0f2"/>
        <stop offset="0.45" stop-color="#6cc6d8"/>
        <stop offset="0.7" stop-color="#b9dcd2"/>
        <stop offset="1" stop-color="#ece6d6"/>
      </linearGradient>
      <radialGradient id="planeTone" cx="0.5" cy="0.5" r="0.5">
        <stop offset="0" stop-color="#f2f4f7" stop-opacity=".85"/>
        <stop offset="1" stop-color="#f2f4f7" stop-opacity="0"/>
      </radialGradient>
    </defs>
    <rect class="front-bg" width="760" height="434" fill="url(#frontGlow)"/>
    <rect class="url-band" x="0" y="0" width="520" height="84" fill="var(--blue-deep)" opacity=".35"/>
    <rect class="beach-photo" role="img" aria-label="Photo of a palm tree on a white sand beach with turquoise sea and a red kayak"
          x="0" y="0" width="760" height="390" fill="url(#beachTone)"
          style="clip-path: polygon(532px 0, 760px 0, 760px 390px, 448px 390px);"/>
    <polygon class="divider-orange" points="522,0 532,0 448,390 438,390" fill="var(--orange)"/>
    <polygon class="divider-yellow" points="512,0 522,0 438,390 428,390" fill="var(--yellow)"/>
    <rect class="bottom-band" x="0" y="390" width="760" height="44" fill="var(--blue-light)"/>
    <ellipse class="airplane" role="img" aria-label="Illustration of a white passenger jet in flight"
             cx="450" cy="130" rx="110" ry="70" fill="url(#planeTone)"/>
    <g class="logo-frame" transform="rotate(-3 227 276)">
      <rect x="70" y="176" width="300" height="200" rx="12" fill="var(--blue-light)"/>
      <rect x="98" y="188" width="290" height="190" rx="12" fill="var(--yellow)"/>
      <rect x="84" y="178" width="290" height="192" rx="12" fill="var(--white)"/>
    </g>
  </svg>
  <p class="front-url">www.sunnypathsjoy.example</p>
  <p class="front-logo">Sunny Paths<br>and joy</p>
</section>

<section class="card card-back">
  <svg class="art" width="760" height="434" viewBox="0 0 760 434">
    <defs>
      <radialGradient id="backGlow" cx="0.1" cy="0.15" r="1">
        <stop offset="0" stop-color="#ffffff"/>
        <stop offset="1" stop-color="#edf4fa"/>
      </radialGradient>
    </defs>
    <rect width="760" height="434" fill="url(#backGlow)"/>
    <rect class="name-marker" x="40" y="58" width="10" height="40" fill="var(--blue)"/>
    <g class="logo-frame">
      <rect x="524" y="52" width="206" height="104" rx="8" fill="var(--blue-light)"/>
      <rect x="540" y="64" width="204" height="102" rx="8" fill="var(--yellow)"/>
      <rect x="530" y="56" width="204" height="102" rx="8" fill="var(--white)"/>
    </g>
  </svg>
  <h1 class="back-name">Leandro T. Ocampo</h1>

  <ul class="contact-list">
    <li><svg viewBox="0 0 14 14"><path d="M3 1h3l1 3-2 1.5a8 8 0 0 0 3.5 3.5L10 7l3 1v3c0 1-1 2-2 2A11 11 0 0 1 1 3c0-1 1-2 2-2z" fill="var(--link)"/></svg>(55) 5000-0142</li>
    <li><svg viewBox="0 0 14 14"><rect x="4" y="1" width="6" height="12" rx="1.2" fill="var(--link)"/><rect x="5" y="2.5" width="4" height="7" fill="#fff"/></svg>(55) 9000-0187</li>
    <li><svg viewBox="0 0 14 14"><rect x="1" y="3" width="12" height="8" fill="var(--link)"/><path d="M1 3l6 4.5L13 3" stroke="#fff" fill="none"/></svg>leandro@sunnypathsjoy.example</li>
    <li class="web"><svg viewBox="0 0 14 14"><circle cx="7" cy="7" r="6" fill="var(--link)"/><path d="M1 7h12M7 1c-3 3-3 9 0 12M7 1c3 3 3 9 0 12" stroke="#fff" stroke-width=".9" fill="none"/></svg>www.sunnypathsjoy.example</li>
    <li><svg viewBox="0 0 14 14"><circle cx="7" cy="7" r="6" fill="var(--link)"/></svg>sunnypathsandjoy.blogsite.example</li>
  </ul>

  <ul class="address">
    <li>Alameda 482, 3 piso</li>
    <li>Col. Tlalpizco</li>
    <li>Mexico, D.F. 07320</li>
    <li class="social"><i></i>SunnyPathsAndJoy</li>
    <li class="social"><i></i>@sunnypjoy</li>
  </ul>

  <p class="back-logo">Sunny Paths<br>and joy</p>
</section>

</body>
</html>
```